New Managed IT company needs a business card

We are an IT management and support company that needs a business card design. I have a logo that I'll provide. Blues and blacks match the logo, but i'm open to anything. I want the card to help people take us seriously, but still have some energy and fun in it. The card should communicate stability and a solid company.

Target Market(s)

Target market includes Owners and Presidents at small businesses of 20 - 100 employees in the Pittsburgh PA area.

Industry/Entity Type

Information Technology

Contact Information for Business Card

i am open to other designs, but i imagine having only the logo on one side and then the logo plus all contact details on the other side.

Requirements
Must have
• Our logo
• Company name is optional if the logo makes it obvious
• A name - Cole Perrin
• A title - President
• A phone number - 724-XXX-XXXX
• A mobile phone number - 724-615-2748
• An email address - cperrin@techvaultgrid.com
• a website - techvaultgrid.com or www.techvaultgrid.com
Nice to have
• some people tell me the logo feels like a superhero theme, some fun with that idea might be good. I'm open to ideas.
Should not have
• stock photos of people or computers - especially old looking stuff.

```html
<!DOCTYPE html>
<html lang="en">
<head>
<meta charset="utf-8">
<title>TechVault Grid – Business Card</title>
<link rel="stylesheet" href="https://fonts.googleapis.com/css2?family=Open+Sans:wght@400;600;700&display=swap">
<style>
  :root {
    --backdrop: #2b2d31;
    --brand-blue: #0a6fd6;
    --brand-blue-deep: #0a47a8;
    --brand-blue-light: #1a9be8;
    --ink: #1b1c1e;
    --ink-soft: #2e2f33;
    --card-white: #ffffff;
    --accent-line: #1b86d6;
  }
  * { margin: 0; padding: 0; box-sizing: border-box; }
  html, body {
    width: 1200px;
    height: 864px;
    overflow: hidden;
    background: var(--backdrop);
    font-family: "Open Sans", Arial, sans-serif;
  }
  .stage {
    position: relative;
    width: 1200px;
    height: 864px;
  }
  .card {
    position: absolute;
    width: 600px;
    height: 340px;
    border-radius: 4px;
    overflow: hidden;
  }
  /* Front side */
  .card-front {
    left: 200px;
    top: 60px;
    background: radial-gradient(ellipse at 55% 35%, var(--brand-blue-light) 0%, var(--brand-blue) 45%, var(--brand-blue-deep) 100%);
  }
  .front-wordmark {
    position: absolute;
    left: 0;
    right: 0;
    top: 190px;
    display: flex;
    align-items: center;
    justify-content: center;
    gap: 16px;
    color: var(--card-white);
    font-weight: 700;
    font-size: 38px;
    letter-spacing: 4px;
    text-transform: uppercase;
  }
  .front-wordmark .mark-dot {
    width: 30px;
    height: 30px;
    border-radius: 50%;
    background: var(--card-white);
  }
  /* Back side */
  .card-back {
    left: 240px;
    top: 460px;
    background: var(--card-white);
  }
  .back-wordmark {
    position: absolute;
    right: 40px;
    top: 52px;
    display: flex;
    align-items: center;
    gap: 14px;
    color: var(--ink);
    font-weight: 700;
    font-size: 32px;
    letter-spacing: 3px;
    text-transform: uppercase;
  }
  .back-wordmark .mark-dot {
    width: 54px;
    height: 54px;
    border-radius: 50%;
    background: var(--brand-blue);
  }
  .holder {
    position: absolute;
    left: 60px;
    top: 160px;
  }
  .holder-name {
    color: var(--brand-blue);
    font-weight: 700;
    font-size: 19px;
    line-height: 1.2;
  }
  .holder-title {
    color: var(--ink-soft);
    font-size: 13px;
  }
  .divider {
    position: absolute;
    left: 220px;
    right: 0;
    top: 198px;
    height: 2px;
    background: var(--accent-line);
  }
  .contact-list {
    position: absolute;
    right: 30px;
    top: 222px;
    list-style: none;
    text-align: right;
  }
  .contact-list li {
    display: flex;
    justify-content: flex-end;
    align-items: center;
    gap: 10px;
    font-size: 15px;
    line-height: 25px;
    color: var(--ink);
  }
  .contact-list svg {
    width: 13px;
    height: 13px;
    fill: var(--brand-blue);
    flex: none;
  }
</style>
</head>
<body>
<main class="stage">
  <section class="card card-front" aria-label="Card front">
    <div class="front-wordmark"><span class="mark-dot"></span><span>TechVault Grid</span></div>
  </section>

  <section class="card card-back" aria-label="Card back">
    <div class="back-wordmark"><span class="mark-dot"></span><span>TechVault Grid</span></div>

    <div class="holder">
      <p class="holder-name">Cole Perrin</p>
      <p class="holder-title">President</p>
    </div>

    <div class="divider"></div>

    <ul class="contact-list">
      <li>724-XXX-XXXX
        <svg viewBox="0 0 16 16" aria-hidden="true"><path d="M3.5 1.5l2.5 0 1.2 3.2-1.6 1.2c.8 1.8 2.2 3.2 4 4l1.2-1.6 3.2 1.2v2.5c0 .8-.7 1.5-1.5 1.5C6.8 13.5 2 8.7 2 3c0-.8.7-1.5 1.5-1.5z"/></svg>
      </li>
      <li>724-615-2748
        <svg viewBox="0 0 16 16" aria-hidden="true"><path d="M4.5 0.5h7c.6 0 1 .4 1 1v13c0 .6-.4 1-1 1h-7c-.6 0-1-.4-1-1v-13c0-.6.4-1 1-1zm.8 2v9.5h5.4V2.5zM8 12.8a.9.9 0 100 1.8.9.9 0 000-1.8z"/></svg>
      </li>
      <li>cperrin@techvaultgrid.com
        <svg viewBox="0 0 16 16" aria-hidden="true"><path d="M1 3h14v10H1zm1.5 1.5v.3L8 8.6l5.5-3.8v-.3zm0 2.1v4.9h11V6.6L8 10.4z"/></svg>
      </li>
      <li>www.techvaultgrid.com
        <svg viewBox="0 0 16 16" aria-hidden="true"><circle cx="8" cy="8" r="7"/></svg>
      </li>
    </ul>
  </section>
</main>
</body>
</html>
```